Cause bitches need love too!

I am creating an ad campaign. It will be a series of featured dogs in our shelter and they will contain a picture of the dog wich should be big enough to see on a yard sign and will change every week. I am placing the signs so that they lead you to the shelter. This is why I am also including the copy that says "you're almost there".

I have 4 tag lines:

1. Find unconditional Love.
2. She'll Love you furever!
3. He'll always listen.
4. Meet your new BFF

You're almost there 217 W Marlowe Ave
Open 10 - 7/Tues-Sat

The dimensions for the sign are 24" wide and 18" high

Every week we will have a different picture of a different dog (hopefully last week's dog gets adopted). Anyhow, I am printing out yard signs, meaning that instead of printing 160 different signs it would be ideal just to replace the photo. So far the copy that is permanent is: "You're almost there. 217 W. Marlowe Ave."

I could silhouette the image of the dog as well and super impose it on the sign, that's also a consideration, but ideally if I could have 4 tag lines I could print 40 signs of each and just replace the photo manually each week from my printer that would save costs.
Updates

Not enough designs to chose from and I edited the brief and committed to pay no matter what to increase the amount of designs as per your suggestions.

Target Market(s)

Animal lovers

Industry/Entity Type

Campaign

Font styles to use
Sans Serif

Colors

Designer to choose colors to be used in the design.

Requirements
Must have
• The dimensions for the sign are 24" wide and 18" high
Nice to have
• I want the signs to be hip, they should have a positive feel to them. You can alter the photos if you like. I am even open to new copy if you think something else works better.

```html
<!DOCTYPE html>
<html lang="en">
<head>
<meta charset="utf-8">
<title>Find unconditional Love – yard sign</title>
<link rel="stylesheet" href="https://fonts.googleapis.com/css2?family=Oswald:wght@500;600;700&display=swap">
<style>
  :root {
    --studio-light: #c9c4c6;
    --studio-mid: #a9a5a7;
    --studio-dark: #8e8c8d;
    --coat-tone: #8d8279;
    --headline-yellow: #fff200;
    --ink: #000000;
    --paper: #ffffff;
    --signal-red: #ed1c24;
  }
  html, body {
    margin: 0;
    padding: 0;
    overflow: hidden;
    background: var(--studio-mid);
  }
  .sign {
    position: relative;
    width: 1200px;
    height: 900px;
    overflow: hidden;
    font-family: "Oswald", "Arial Narrow", sans-serif;
    background: linear-gradient(160deg, var(--studio-light) 0%, var(--studio-mid) 55%, var(--studio-dark) 100%);
  }
  .dog-photo {
    position: absolute;
    left: 0;
    top: 190px;
    width: 820px;
    height: 602px;
    background: radial-gradient(ellipse at 45% 45%, var(--coat-tone) 0%, #7c736c 55%, rgba(142,140,141,0) 78%);
  }
  .headline {
    position: absolute;
    left: 0;
    top: 0;
    width: 1200px;
    height: 260px;
  }
  .headline text {
    font-family: "Oswald", "Arial Narrow", sans-serif;
    font-weight: 700;
    font-size: 96px;
  }
  .headline .shadow { fill: var(--ink); }
  .headline .face { fill: var(--headline-yellow); }
  .badge {
    position: absolute;
    left: 850px;
    top: 238px;
    width: 260px;
    height: 260px;
  }
  .badge-text {
    position: absolute;
    left: 850px;
    top: 238px;
    width: 260px;
    height: 260px;
    display: flex;
    flex-direction: column;
    align-items: center;
    justify-content: center;
    color: var(--paper);
    font-weight: 600;
    line-height: 0.88;
    text-align: center;
    transform: rotate(-20deg);
  }
  .badge-text span { display: block; }
  .badge-text .badge-line { font-size: 50px; }
  .directions {
    position: absolute;
    left: 640px;
    top: 510px;
    width: 540px;
    text-align: center;
  }
  .almost-there {
    margin: 0;
    color: var(--paper);
    font-weight: 500;
    font-size: 68px;
    line-height: 1.1;
    letter-spacing: -1px;
  }
  .address {
    margin: 0;
    color: var(--ink);
    font-weight: 600;
    line-height: 1;
    font-style: normal;
  }
  .address .street-number { display: block; font-size: 88px; margin-top: 2px; }
  .address .street-name { display: block; font-size: 74px; margin-top: -2px; letter-spacing: -1px; }
  .hours-band {
    position: absolute;
    left: 0;
    top: 792px;
    width: 1200px;
    height: 108px;
    background: var(--signal-red);
  }
  .hours {
    position: absolute;
    left: 0;
    top: 0;
    width: 1168px;
    margin: 0;
    text-align: center;
    color: var(--paper);
    font-weight: 500;
    font-size: 80px;
    line-height: 108px;
    letter-spacing: -1px;
  }
</style>
</head>
<body>
<main class="sign">
  <div class="dog-photo" role="img" aria-label="Photo of the featured shelter dog of the week, a grey and white pit bull mix looking up"></div>

  <svg class="headline" viewBox="0 0 1200 260" aria-label="Find unconditional Love">
    <defs>
      <path id="headline-arc" d="M 95 250 Q 600 30 1100 250"/>
      <path id="headline-arc-shadow" d="M 100 255 Q 605 35 1105 255"/>
    </defs>
    <text class="shadow"><textPath href="#headline-arc-shadow" startOffset="50%" text-anchor="middle">Find unconditional Love</textPath></text>
    <text class="face"><textPath href="#headline-arc" startOffset="50%" text-anchor="middle">Find unconditional Love</textPath></text>
  </svg>

  <svg class="badge" viewBox="0 0 260 260" aria-hidden="true">
    <g fill="var(--signal-red)">
      <rect x="38" y="38" width="184" height="184" transform="rotate(0 130 130)"/>
      <rect x="38" y="38" width="184" height="184" transform="rotate(11.25 130 130)"/>
      <rect x="38" y="38" width="184" height="184" transform="rotate(22.5 130 130)"/>
      <rect x="38" y="38" width="184" height="184" transform="rotate(33.75 130 130)"/>
      <rect x="38" y="38" width="184" height="184" transform="rotate(45 130 130)"/>
      <rect x="38" y="38" width="184" height="184" transform="rotate(56.25 130 130)"/>
      <rect x="38" y="38" width="184" height="184" transform="rotate(67.5 130 130)"/>
      <rect x="38" y="38" width="184" height="184" transform="rotate(78.75 130 130)"/>
    </g>
  </svg>
  <p class="badge-text">
    <span class="badge-line">Meet</span>
    <span class="badge-line">your new</span>
    <span class="badge-line">BFF</span>
  </p>

  <section class="directions">
    <h2 class="almost-there">You're almost there</h2>
    <address class="address">
      <span class="street-number">217 W</span>
      <span class="street-name">Marlowe Ave</span>
    </address>
  </section>

  <footer class="hours-band">
    <p class="hours">Open 10 - 7/Tues-Sat</p>
  </footer>
</main>
</body>
</html>
```